Environmental "Pledge" Website

We are creating a template for a pledge campaign. Local residents visit a website and fill out a form. If they fill out the form and promise to do something good for the environment, they might win a prize.

They can watch a YouTube video that explains the contest. They can see a Google Map of everybody that has signed the pledge.

There is a blog on the homepage so the can see how the contest is going.

Campaign

```html
<!DOCTYPE html>
<html lang="en">
<head>
<meta charset="utf-8">
<title>Pledge Campaign</title>
<link href="https://fonts.googleapis.com/css2?family=Roboto:wght@300;400;500&display=swap" rel="stylesheet">
<style>
:root{
  --ink:#333333;
  --text:#555555;
  --accent:#e8a317;
  --orange:#f08a24;
  --grey-band:#f3f3f3;
  --footer:#333333;
  --footer-text:#9a9a9a;
  --white:#ffffff;
  --rule:#444444;
}
*{box-sizing:border-box;margin:0;padding:0}
html,body{width:780px;height:1200px;overflow:hidden}
body{font-family:'Roboto',sans-serif;color:var(--text);background:var(--white);position:relative}

.hero{position:relative;height:388px;background:linear-gradient(180deg,#8a7762 0%,#6f5b48 40%,#4d3d31 75%,#3e322a 100%);overflow:hidden}
.hero-photo{position:absolute;inset:0;background:
  linear-gradient(180deg,rgba(150,135,115,.55) 0%,rgba(0,0,0,0) 45%),
  linear-gradient(90deg,rgba(60,45,35,.4),rgba(120,100,80,.1) 50%,rgba(60,45,35,.4))}
.main-nav{position:absolute;top:0;left:0;right:0;height:55px;border-bottom:1px solid rgba(255,255,255,.25);display:flex;justify-content:center;gap:0}
.main-nav a{color:var(--white);font-size:9.5px;font-weight:400;letter-spacing:.3px;text-decoration:none;padding:0 12.5px;line-height:69px;height:56px;position:relative}
.main-nav a.active::after{content:"";position:absolute;left:0;right:0;bottom:-1px;height:3px;background:var(--orange)}
.slide-arrow{position:absolute;top:164px;width:18px;height:60px}
.slide-arrow.prev{left:49px}
.slide-arrow.next{right:48px}
.campaign-card{position:absolute;left:293px;top:92px;width:194px;height:228px;background:rgba(30,26,24,.85);text-align:center;padding:12px 12px 0}
.campaign-card .rule{height:2px;background:#6a6a6a}
.brand{display:flex;align-items:center;justify-content:center;gap:10px;height:82px}
.brand-dot{width:22px;height:22px;border-radius:50%;background:var(--accent)}
.brand-name{color:var(--white);font-weight:300;font-size:17px;line-height:20px;text-align:left;letter-spacing:.5px}
.tagline{color:var(--accent);font-size:10.5px;font-weight:400;line-height:16.5px;margin-top:12px;letter-spacing:.2px}
.lead{color:#e6e6e6;font-size:10px;margin-top:4px}
.pledge-btn{display:inline-block;margin-top:14px;border:2px solid var(--white);color:var(--white);font-size:13px;font-weight:500;letter-spacing:.6px;padding:6px 15px;text-decoration:none}

.welcome{height:154px;text-align:center;padding-top:33px}
.section-title{font-size:17px;font-weight:500;color:var(--ink);letter-spacing:.5px}
.title-rule{width:98px;height:1px;background:var(--rule);margin:12px auto 0}
.welcome p{font-size:8.4px;line-height:16.8px;font-weight:300;color:var(--text);width:600px;margin:14px auto 0}

.feature-band{background:var(--grey-band);height:283px;position:relative}
.feature{position:absolute;top:26px;width:320px;text-align:center}
.feature.video{left:49px}
.feature.map{left:412px}
.feature .section-title{font-size:16.5px}
.media{margin-top:14px;height:195px;position:relative}
.video .media{background:linear-gradient(135deg,#8a8a8a,#6d6d6d 55%,#9a7a62)}
.map .media{background:linear-gradient(135deg,#eee9dd,#e4eddc);border:2px solid #c9c9c9}
.play-btn{position:absolute;left:140px;top:83px;width:40px;height:28px;border-radius:7px;background:var(--white)}
.play-btn::after{content:"";position:absolute;left:16px;top:8px;border-left:11px solid #333;border-top:6px solid transparent;border-bottom:6px solid transparent}
.pin{position:absolute;left:172px;top:78px}

.blog{height:305px;text-align:center;padding-top:36px}
.posts{display:flex;justify-content:space-between;width:680px;margin:22px auto 0}
.post{width:213px}
.post-thumb{height:116px;border:2px solid #d5d5d5}
.post:nth-child(1) .post-thumb{background:linear-gradient(120deg,#f2c27a,#b56a2e 55%,#3a2a22)}
.post:nth-child(2) .post-thumb{background:linear-gradient(135deg,#5b5450,#8a7a6d 50%,#4a4240)}
.post:nth-child(3) .post-thumb{background:linear-gradient(135deg,#d8dde2,#6f7378 50%,#2f3236)}
.post-title{color:var(--accent);font-size:9.2px;font-weight:500;letter-spacing:.3px;margin-top:14px}
.post-excerpt{font-size:8.8px;line-height:13.6px;color:var(--text);margin-top:6px}
.post-date{font-size:8.6px;color:var(--ink);font-weight:500;margin-top:10px;display:flex;align-items:center;justify-content:center;gap:4px}

.site-footer{position:absolute;left:0;right:0;bottom:0;height:70px;background:var(--footer);display:flex;align-items:center;justify-content:space-between;padding:0 48px 0 49px}
.copyright{font-size:8.3px;color:var(--footer-text);font-weight:300}
.social{display:flex;gap:15px}
.social span{width:13px;height:13px;border-radius:50%;background:#bdbdbd;display:block}
</style>
</head>
<body>

<header class="hero">
  <div class="hero-photo" role="img" aria-label="City skyline seen from above in warm sepia tones"></div>
  <nav class="main-nav">
    <a class="active" href="#">HOME</a>
    <a href="#">ABOUT US</a>
    <a href="#">FINE PRINT</a>
    <a href="#">WHY PLEDGE</a>
    <a href="#">PLEDGE MAP</a>
    <a href="#">UPDATES</a>
  </nav>
  <svg class="slide-arrow prev" viewBox="0 0 18 60"><polyline points="16,1 2,30 16,59" fill="none" stroke="#fff" stroke-width="1.3"/></svg>
  <svg class="slide-arrow next" viewBox="0 0 18 60"><polyline points="2,1 16,30 2,59" fill="none" stroke="#fff" stroke-width="1.3"/></svg>
  <div class="campaign-card">
    <div class="rule"></div>
    <div class="brand">
      <span class="brand-dot"></span>
      <span class="brand-name">PLEDGE<br>CAMPAIGN</span>
    </div>
    <div class="rule"></div>
    <p class="tagline">DO SOMETHING GOOD FOR THE<br>ENVIRONMENT</p>
    <p class="lead">Aenean a nibh eget turpis vehicula</p>
    <a class="pledge-btn" href="#">PLEDGE NOW</a>
  </div>
</header>

<section class="welcome">
  <h2 class="section-title">WELCOME TO OUR WEBSITE</h2>
  <div class="title-rule"></div>
  <p>Aliquam molestie, mi et imperdiet euismod, dui purus auctor tellus, et interdum lacus lectus et ante. Sed accumsan sollicitudin sapien, sit amet adipiscing turpis gravida ac. In congue, neque ac lobortis volutpat, libero mauris varius mi, vitae suscipit ipsum ligula vitae risus. Duis aliquam nibh a dui iaculis viverra id a velit. Vivamus egestas risus in magna varius commodo. Sed semper viverra egestas.</p>
</section>

<section class="feature-band">
  <div class="feature video">
    <h2 class="section-title">WHAT’S THIS ABOUT</h2>
    <div class="media" role="img" aria-label="Video still of hands holding a young tree seedling in soil">
      <span class="play-btn"></span>
    </div>
  </div>
  <div class="feature map">
    <h2 class="section-title">WHO’S PLEDGE</h2>
    <div class="media" role="img" aria-label="Street map showing where pledges have been signed">
      <svg class="pin" width="10" height="14" viewBox="0 0 10 14"><path d="M5 0a5 5 0 0 1 5 5c0 4-5 9-5 9S0 9 0 5a5 5 0 0 1 5-5z" fill="#d9342b"/><circle cx="5" cy="5" r="1.8" fill="#7a1a14"/></svg>
    </div>
  </div>
</section>

<section class="blog">
  <h2 class="section-title">BLOG POSTS</h2>
  <div class="title-rule"></div>
  <div class="posts">
    <article class="post">
      <div class="post-thumb" role="img" aria-label="Group raising hands together at sunset"></div>
      <h3 class="post-title">DUIS ALIQUAM NIBH A DUI IACULIS.</h3>
      <p class="post-excerpt">Vivamus egestas risus in magna varius commodo.<br>Sed semper viverra egestas.</p>
      <p class="post-date"><svg width="9" height="9" viewBox="0 0 9 9"><rect x=".5" y="1.5" width="8" height="7" fill="none" stroke="#8a5a3a"/><rect x=".5" y="1.5" width="8" height="2" fill="#8a5a3a"/></svg>Dec10, 2015</p>
    </article>
    <article class="post">
      <div class="post-thumb" role="img" aria-label="Crowd of people standing with hands on hearts"></div>
      <h3 class="post-title">DUIS ALIQUAM NIBH A DUI IACULIS.</h3>
      <p class="post-excerpt">Vivamus egestas risus in magna varius commodo.<br>Sed semper viverra egestas.</p>
      <p class="post-date"><svg width="9" height="9" viewBox="0 0 9 9"><rect x=".5" y="1.5" width="8" height="7" fill="none" stroke="#8a5a3a"/><rect x=".5" y="1.5" width="8" height="2" fill="#8a5a3a"/></svg>Dec10, 2015</p>
    </article>
    <article class="post">
      <div class="post-thumb" role="img" aria-label="Team stacking hands together in a circle"></div>
      <h3 class="post-title">DUIS ALIQUAM NIBH A DUI IACULIS.</h3>
      <p class="post-excerpt">Vivamus egestas risus in magna varius commodo.<br>Sed semper viverra egestas.</p>
      <p class="post-date"><svg width="9" height="9" viewBox="0 0 9 9"><rect x=".5" y="1.5" width="8" height="7" fill="none" stroke="#8a5a3a"/><rect x=".5" y="1.5" width="8" height="2" fill="#8a5a3a"/></svg>Dec10, 2015</p>
    </article>
  </div>
</section>

<footer class="site-footer">
  <p class="copyright">Copyright © 2015. Company Name All Right Reserved</p>
  <div class="social" aria-label="Social links">
    <span></span><span></span><span></span><span></span><span></span><span></span>
  </div>
</footer>

</body>
</html>
```